Business Cards Needed for Innovative Healthcare Marketing Company

We are a marketing company focused on healthcare. Our company is all about rebranding yourself renewing your image and generating results. The phoenix stands for "reborn" or "rising" which we provide new brands for our clients we take their old brands and renew it with creativity and innovation. I am looking for a business card with color dimension. I have attached an example of a card I think has the look and feel of what I am trying to accomplish. I like that the card example has black and grey font colors, I like the font placement and the small logo, I really like the use of the colors on the right those are the colors of my logo. My logo is phoenix so maybe incorporating flames similar to that design. I would like the back a solid color maybe red with an opaque version of the logo and website. As a marketing company I am always open to creative liberty!

Target Market(s)

Doctors and business professionals.

Industry/Entity Type

Marketing

Contact Information for Business Card

Velmora Health Care Marketing
Dana Prewitt- CEO
#(407)555-0172
email-dana@velmora.com
website- velmora.com

Font styles to use
Sans Serif

Colors
ec1f27
f37122
ffc214
fbed22
fbf289
f04a50

Requirements
Must have
• The logo and required information
Nice to have
• icons by the information
Should not have
• child like font

```html
<!DOCTYPE html>
<html lang="en">
<head>
<meta charset="utf-8">
<title>Velmora Health Care Marketing – Business Card</title>
<link rel="stylesheet" href="https://fonts.googleapis.com/css2?family=Open+Sans:wght@400;600;700&display=swap">
<style>
  :root {
    --stage: #3b3b3b;
    --card-black: #0a0a0a;
    --card-white: #ffffff;
    --brand-red: #b3242b;
    --brand-orange: #f37122;
    --brand-amber: #f7931e;
    --text-grey: #555555;
    --rule-grey: #9a9a9a;
  }
  * { margin: 0; padding: 0; box-sizing: border-box; }
  html, body {
    width: 1200px; height: 950px; overflow: hidden;
    background: var(--stage);
    font-family: "Open Sans", Arial, sans-serif;
  }
  .sheet {
    position: relative; width: 1200px; height: 950px;
  }
  .card {
    position: absolute; left: 250px; width: 700px; height: 400px;
    overflow: hidden;
    box-shadow: 0 10px 30px rgba(0,0,0,.45);
  }
  .card--back { top: 50px; background: var(--card-black); }
  .card--front { top: 500px; background: var(--card-black); }

  .back-mark {
    position: absolute; inset: 0;
    display: flex; align-items: center; justify-content: center; gap: 14px;
  }
  .back-mark__dot {
    width: 22px; height: 22px; border-radius: 50%; background: var(--card-white);
  }
  .back-mark__name {
    color: var(--card-white); font-weight: 600; font-size: 40px; letter-spacing: 4px;
  }

  .front-shape { position: absolute; inset: 0; }

  .brand {
    position: absolute; top: 48px; right: 80px;
    display: flex; align-items: center; gap: 12px;
  }
  .brand__dot {
    width: 26px; height: 26px; border-radius: 50%; background: var(--brand-orange);
  }
  .brand__name {
    color: var(--brand-red); font-weight: 400; font-size: 19px; letter-spacing: 1.5px;
    line-height: 1.2; text-align: left;
  }

  .divider {
    position: absolute; left: 70px; right: 70px; top: 248px;
    height: 1px; background: var(--rule-grey);
  }
  .person {
    position: absolute; left: 78px; top: 268px;
    font-weight: 700; font-size: 24px; color: var(--brand-red); letter-spacing: .5px;
  }
  .person__role { color: var(--brand-orange); }

  .contacts {
    position: absolute; left: 78px; top: 318px;
    display: flex; gap: 22px; align-items: center;
    color: var(--text-grey); font-size: 17px;
  }
  .contact { display: flex; align-items: center; gap: 7px; }
  .contact svg { width: 18px; height: 18px; fill: var(--brand-red); flex: none; }
</style>
</head>
<body>
<main class="sheet">

  <section class="card card--back" aria-label="Card back">
    <div class="back-mark">
      <span class="back-mark__dot"></span>
      <span class="back-mark__name">VELMORA</span>
    </div>
  </section>

  <section class="card card--front" aria-label="Card front">
    <svg class="front-shape" viewBox="0 0 700 400" width="700" height="400" aria-hidden="true">
      <path d="M40 0 H660 Q745 200 660 400 H40 Q-45 200 40 0 Z" fill="var(--card-white)"/>
      <path d="M52 60 Q-2 200 52 360" fill="none" stroke="var(--brand-orange)" stroke-width="7" stroke-linecap="round"/>
      <path d="M648 40 Q706 200 648 370" fill="none" stroke="var(--brand-red)" stroke-width="7" stroke-linecap="round"/>
    </svg>

    <div class="brand">
      <span class="brand__dot"></span>
      <span class="brand__name">VELMORA<br>HEALTH CARE MARKETING</span>
    </div>

    <div class="divider"></div>

    <p class="person">DANA PREWITT - <span class="person__role">CEO</span></p>

    <div class="contacts">
      <span class="contact">
        <svg viewBox="0 0 24 24" aria-hidden="true"><path d="M6.6 10.8a15 15 0 0 0 6.6 6.6l2.2-2.2c.3-.3.7-.4 1-.2 1.1.4 2.3.6 3.6.6.6 0 1 .4 1 1V20c0 .6-.4 1-1 1A17 17 0 0 1 3 4c0-.6.4-1 1-1h3.5c.6 0 1 .4 1 1 0 1.3.2 2.5.6 3.6.1.3 0 .7-.2 1z"/></svg>
        (407)555-0172
      </span>
      <span class="contact">
        <svg viewBox="0 0 24 24" aria-hidden="true"><path d="M2 5h20v14H2z M3 6l9 7 9-7" /><path d="M2 5h20L12 12z" fill="#fff" opacity=".6"/></svg>
        dana@velmora.com
      </span>
      <span class="contact">
        <svg viewBox="0 0 24 24" aria-hidden="true"><path d="M12 2a10 10 0 1 0 0 20 10 10 0 0 0 0-20zm6.9 6h-3a15 15 0 0 0-1.3-4A8 8 0 0 1 18.9 8zM12 4c.8 1.1 1.5 2.5 1.9 4h-3.8c.4-1.5 1.1-2.9 1.9-4zM4.3 14a8 8 0 0 1 0-4h3.4a16 16 0 0 0 0 4zm.8 2h3a15 15 0 0 0 1.3 4A8 8 0 0 1 5.1 16zm3-8h-3a8 8 0 0 1 4.3-4 15 15 0 0 0-1.3 4zM12 20c-.8-1.1-1.5-2.5-1.9-4h3.8c-.4 1.5-1.1 2.9-1.9 4zm2.3-6H9.7a14 14 0 0 1 0-4h4.6a14 14 0 0 1 0 4zm.3 5.6a15 15 0 0 0 1.3-3.6h3a8 8 0 0 1-4.3 3.6zm1.7-5.6a16 16 0 0 0 0-4h3.4a8 8 0 0 1 0 4z"/></svg>
        www.velmora.com
      </span>
    </div>
  </section>

</main>
</body>
</html>
```